flat share room mate rental website(design only)

We need a design for the homepage of a flat share / roommate website. We have a website template http://demo1.lodgeframe.net and we're looking for a homepage similar to this http://uk.bunkpalhub.com but different.
The main user of the site are likely to be students and young professionals so were not looking for anything too serious.
We want to emphasise that the website will be 100% free to use both to post an advert and to contact the advertiser.
We must have a 'new rooms' and new flatmates carousel, also we would prefer if the menu had only a login button and maybe a 'post a room' button.
Our logo is currently being designed, so you can put anything in its place.
We look forward to seeing what you guys come up with.
Target Market(s)
Students, Young Professionals
Industry/Entity Type
Rental
Number of Pages Required
1 page
Look and feel
Each slider illustrates characteristics of the customer's brand and the style your logo design should communicate.

```html
<!DOCTYPE html>
<html lang="en">
<head>
<meta charset="utf-8">
<title>Flatmate Finder – Home</title>
<link href="https://fonts.googleapis.com/css2?family=Oswald:wght@400;500&family=Open+Sans:wght@400;600;700&display=swap" rel="stylesheet">
<style>
:root{
  --orange:#f6a23a;
  --pink:#f39199;
  --ink:#2b2b2b;
  --body:#666;
  --grey-band:#e4e4e4;
  --cta-band:#e9e9e9;
  --footer:#232323;
  --footer-text:#9a9a9a;
  --white:#fff;
}
*{margin:0;padding:0;box-sizing:border-box}
html,body{width:1200px;height:3090px;overflow:hidden}
body{font-family:"Open Sans",Arial,sans-serif;color:var(--body);background:var(--white);position:relative}
.head-font{font-family:"Oswald","Arial Narrow",sans-serif}

/* hero */
.hero{position:absolute;left:0;top:0;width:1200px;height:639px;
  background:linear-gradient(100deg,#2d2f33 0%,#4a4a48 35%,#6d5a45 62%,#b7743d 82%,#7a5538 100%)}
.hero-bar{position:absolute;left:0;top:0;width:100%;height:72px;background:rgba(0,0,0,.55)}
.logo{position:absolute;left:72px;top:20px;font-family:"Oswald",sans-serif;font-size:22px;font-weight:500;color:var(--white);letter-spacing:.5px}
.menu{position:absolute;right:72px;top:26px;display:flex;gap:26px}
.menu a{font-family:"Oswald",sans-serif;font-size:15px;color:var(--white);text-decoration:none;text-transform:uppercase}
.hero-title{position:absolute;top:232px;left:0;width:100%;text-align:center;font-family:"Oswald",sans-serif;font-size:44px;font-weight:400;color:var(--white);letter-spacing:.5px}
.search{position:absolute;top:340px;left:206px;width:788px;height:60px;background:rgba(255,255,255,.3);display:flex;align-items:center;padding:0 20px;gap:10px}
.search-select{width:400px;height:38px;background:var(--white);display:flex;align-items:center;justify-content:space-between;padding:0 14px;font-size:13px;color:#888}
.btn{height:38px;display:flex;align-items:center;justify-content:center;font-family:"Oswald",sans-serif;font-size:15px;color:var(--white);text-transform:uppercase}
.btn-orange{background:var(--orange)}
.btn-pink{background:var(--pink)}
.search .btn{width:160px}
.hero-note{position:absolute;top:433px;left:0;width:100%;text-align:center;font-family:"Oswald",sans-serif;font-size:17px;color:var(--white);line-height:26px;text-transform:uppercase}
.hero-note strong{color:var(--orange);font-weight:400}

/* section shared */
.section-title{position:absolute;left:72px;font-family:"Oswald",sans-serif;font-size:22px;color:var(--ink);text-transform:uppercase}
.arrows{position:absolute;left:1076px;display:flex;gap:8px}
.arrows span{width:22px;height:22px;background:var(--orange);display:flex;align-items:center;justify-content:center}
.cards{position:absolute;left:72px;display:flex;gap:26px}
.card{width:245px}
.card-photo{width:245px}
.card-bar{height:24px;background:var(--orange);display:flex;align-items:center;justify-content:space-between;padding:0 8px;font-size:12px;color:var(--white)}
.card-bar .who{display:flex;align-items:center;gap:6px}
.card-bar .price{font-weight:700;color:#333;font-size:13px}
.card-text{margin-top:14px;font-size:12.5px;line-height:22px;color:var(--body)}

/* stats */
.stats{position:absolute;left:0;top:1038px;width:1200px;height:412px;background:linear-gradient(135deg,#e9e9e9,#dcdcdc 50%,#e7e7e7)}
.stats-title{position:absolute;top:52px;width:100%;text-align:center;font-family:"Oswald",sans-serif;font-size:22px;color:var(--ink);text-transform:uppercase}
.feature{position:absolute;top:108px;width:330px;text-align:center}
.feature-icon{width:128px;height:128px;border-radius:50%;background:var(--white);margin:0 auto;display:flex;align-items:center;justify-content:center}
.feature h3{margin-top:30px;font-family:"Oswald",sans-serif;font-weight:400;font-size:17px;color:var(--ink);text-transform:uppercase}
.feature p{margin-top:10px;font-size:12.5px;line-height:21px}

/* banner */
.banner{position:absolute;left:0;top:1849px;width:1200px;height:232px;background:linear-gradient(90deg,#5a3d34,#7a5a4e 45%,#4c3630);display:flex;align-items:center;justify-content:center}
.banner h2{font-family:"Oswald",sans-serif;font-weight:400;font-size:44px;line-height:50px;color:var(--white);text-align:center;text-transform:uppercase}

/* cta */
.cta{position:absolute;left:0;top:2480px;width:1200px;height:172px;background:var(--cta-band)}
.cta h2{position:absolute;top:40px;width:100%;text-align:center;font-family:"Oswald",sans-serif;font-weight:400;font-size:22px;color:var(--ink);text-transform:uppercase}
.cta-buttons{position:absolute;top:92px;left:394px;display:flex;gap:13px}
.cta-buttons .btn{width:198px;height:39px}

/* footer */
.footer{position:absolute;left:0;top:2652px;width:1200px;height:438px;background:var(--footer)}
.foot-col{position:absolute;top:56px;width:250px}
.foot-col h4{font-family:"Oswald",sans-serif;font-weight:400;font-size:14px;color:var(--white);text-transform:uppercase;margin-bottom:8px}
.foot-col li{list-style:none;font-size:12.5px;line-height:22px;color:var(--footer-text)}
.foot-col li.all{color:var(--white);font-weight:600;margin-top:8px}
.socials{display:flex;gap:6px;margin-top:4px}
.socials span{width:24px;height:24px;border:1.5px solid #777;border-radius:50%}
.foot-bottom{position:absolute;left:72px;right:72px;top:388px;display:flex;justify-content:space-between;font-size:12px;color:var(--footer-text)}
.foot-bottom nav{display:flex;gap:14px}
</style>
</head>
<body>

<header class="hero" role="img" aria-label="City skyline at sunset seen from above">
  <div class="hero-bar">
    <div class="logo">LOGO HERE</div>
    <nav class="menu"><a href="#">Login</a><a href="#">Post a Room</a></nav>
  </div>
  <h1 class="hero-title">FIND YOUR PERFECT FLATMATE</h1>
  <form class="search">
    <div class="search-select">Select a location
      <svg width="12" height="8" viewBox="0 0 12 8"><path d="M1 1l5 5 5-5" fill="none" stroke="#888" stroke-width="1.6"/></svg>
    </div>
    <div class="btn btn-orange">I need a room</div>
    <div class="btn btn-pink">I have a room</div>
  </form>
  <p class="hero-note"><strong>No fees.</strong> We don't charge you anything.<br>That means no fees to post an advert and no fees to contact your potential new flatmate.</p>
</header>

<!-- New rooms -->
<h2 class="section-title" style="top:680px">New Rooms to Rent</h2>
<div class="arrows" style="top:682px">
  <span><svg width="8" height="10"><path d="M6 1L2 5l4 4" fill="none" stroke="#fff" stroke-width="2"/></svg></span>
  <span><svg width="8" height="10"><path d="M2 1l4 4-4 4" fill="none" stroke="#fff" stroke-width="2"/></svg></span>
</div>
<div class="cards" style="top:734px">
  <article class="card">
    <div class="card-photo" role="img" aria-label="Bedroom with dark wood furniture" style="height:142px;background:linear-gradient(135deg,#5a3b24,#a77b4f 60%,#d9c4a4)"></div>
    <div class="card-bar"><span class="who"><svg width="10" height="13" viewBox="0 0 10 13"><path d="M5 12S1 7 1 4.5a4 4 0 018 0C9 7 5 12 5 12z" fill="#fff"/></svg>Wolverhampton</span><span class="price">$250</span></div>
    <p class="card-text">In publishing and graphic design, lorem ipsum is a filler text commonly used to demonstrate the graphic elements of a document or visual presentation.</p>
  </article>
  <article class="card">
    <div class="card-photo" role="img" aria-label="Bright student room with desk" style="height:142px;background:linear-gradient(135deg,#e9dcc6,#f4ede2 50%,#c9b59a)"></div>
    <div class="card-bar"><span class="who"><svg width="10" height="13" viewBox="0 0 10 13"><path d="M5 12S1 7 1 4.5a4 4 0 018 0C9 7 5 12 5 12z" fill="#fff"/></svg>Wolverhampton</span><span class="price">$250</span></div>
    <p class="card-text">In publishing and graphic design, lorem ipsum is a filler text commonly used to demonstrate the graphic elements of a document or visual presentation.</p>
  </article>
  <article class="card">
    <div class="card-photo" role="img" aria-label="Light bedroom with white bedding" style="height:142px;background:linear-gradient(135deg,#8f8d8a,#d5d2cd 55%,#b2aea8)"></div>
    <div class="card-bar"><span class="who"><svg width="10" height="13" viewBox="0 0 10 13"><path d="M5 12S1 7 1 4.5a4 4 0 018 0C9 7 5 12 5 12z" fill="#fff"/></svg>Wolverhampton</span><span class="price">$250</span></div>
    <p class="card-text">In publishing and graphic design, lorem ipsum is a filler text commonly used to demonstrate the graphic elements of a document or visual presentation.</p>
  </article>
  <article class="card">
    <div class="card-photo" role="img" aria-label="Double bed in a neutral bedroom" style="height:142px;background:linear-gradient(135deg,#efe8df,#d8c8b3 55%,#a98d70)"></div>
    <div class="card-bar"><span class="who"><svg width="10" height="13" viewBox="0 0 10 13"><path d="M5 12S1 7 1 4.5a4 4 0 018 0C9 7 5 12 5 12z" fill="#fff"/></svg>Wolverhampton</span><span class="price">$250</span></div>
    <p class="card-text">In publishing and graphic design, lorem ipsum is a filler text commonly used to demonstrate the graphic elements of a document or visual presentation.</p>
  </article>
</div>

<!-- Stats -->
<section class="stats">
  <h2 class="stats-title">5,456,267 Happy Flatshares and Counting...</h2>
  <div class="feature" style="left:75px">
    <div class="feature-icon"><svg width="50" height="64" viewBox="0 0 50 64"><path d="M25 61S4 36 4 23a21 21 0 0142 0c0 13-21 38-21 38z" fill="none" stroke="var(--orange)" stroke-width="3"/><circle cx="25" cy="23" r="8" fill="none" stroke="var(--orange)" stroke-width="3"/></svg></div>
    <h3>Great Rooms</h3>
    <p>In publishing and graphic design, lorem ipsum is a filler text commonly used to demonstrate the graphic elements of a document or visual presentation.</p>
  </div>
  <div class="feature" style="left:435px">
    <div class="feature-icon"><svg width="60" height="60" viewBox="0 0 60 60"><circle cx="24" cy="24" r="17" fill="none" stroke="#2ab3c9" stroke-width="3"/><path d="M37 37l17 17" stroke="#2ab3c9" stroke-width="4" stroke-linecap="round"/></svg></div>
    <h3>Easy Search</h3>
    <p>In publishing and graphic design, lorem ipsum is a filler text commonly used to demonstrate the graphic elements of a document or visual presentation.</p>
  </div>
  <div class="feature" style="left:795px">
    <div class="feature-icon"><svg width="60" height="56" viewBox="0 0 60 56"><path d="M16 4h40v28H44l-6 7v-7H16z" fill="none" stroke="#3cb89b" stroke-width="3"/><path d="M10 16H4v26h8v8l8-8h16v-4" fill="none" stroke="#3cb89b" stroke-width="3"/><path d="M24 14h24M24 21h24" stroke="#3cb89b" stroke-width="3"/></svg></div>
    <h3>Expert Help 24/7</h3>
    <p>In publishing and graphic design, lorem ipsum is a filler text commonly used to demonstrate the graphic elements of a document or visual presentation.</p>
  </div>
</section>

<!-- Community -->
<h2 class="section-title" style="top:1491px">Our Community</h2>
<div class="arrows" style="top:1494px">
  <span><svg width="8" height="10"><path d="M6 1L2 5l4 4" fill="none" stroke="#fff" stroke-width="2"/></svg></span>
  <span><svg width="8" height="10"><path d="M2 1l4 4-4 4" fill="none" stroke="#fff" stroke-width="2"/></svg></span>
</div>
<div class="cards" style="top:1545px">
  <article class="card">
    <div class="card-photo" role="img" aria-label="Portrait of community member Chris" style="height:142px;background:linear-gradient(135deg,#c9a46a,#e8d3ae 55%,#6f5b45)"></div>
    <div class="card-bar"><span class="who">Chris</span><span class="price" style="font-weight:400;font-size:12px">16-Sep-2014</span></div>
    <p class="card-text">In publishing and graphic design, lorem ipsum is a filler text commonly used to demonstrate the graphic elements of a document or visual presentation.</p>
  </article>
  <article class="card">
    <div class="card-photo" role="img" aria-label="Portrait of community member Jack in a library" style="height:142px;background:linear-gradient(135deg,#7a5a3e,#b89270 55%,#4f6b8c)"></div>
    <div class="card-bar"><span class="who">Jack</span><span class="price" style="font-weight:400;font-size:12px">18-Aug-2014</span></div>
    <p class="card-text">In publishing and graphic design, lorem ipsum is a filler text commonly used to demonstrate the graphic elements of a document or visual presentation.</p>
  </article>
  <article class="card">
    <div class="card-photo" role="img" aria-label="Portrait of community member Laura" style="height:142px;background:linear-gradient(135deg,#6b4d35,#3aa0c9 55%,#a47a5a)"></div>
    <div class="card-bar"><span class="who">Laura</span><span class="price" style="font-weight:400;font-size:12px">12-Sep-2014</span></div>
    <p class="card-text">In publishing and graphic design, lorem ipsum is a filler text commonly used to demonstrate the graphic elements of a document or visual presentation.</p>
  </article>
  <article class="card">
    <div class="card-photo" role="img" aria-label="Portrait of community member John" style="height:142px;background:linear-gradient(135deg,#d9e2e8,#4d3a2e 55%,#c4d0d8)"></div>
    <div class="card-bar"><span class="who">John</span><span class="price" style="font-weight:400;font-size:12px">12-Sep-2014</span></div>
    <p class="card-text">In publishing and graphic design, lorem ipsum is a filler text commonly used to demonstrate the graphic elements of a document or visual presentation.</p>
  </article>
</div>

<!-- Banner -->
<section class="banner" role="img" aria-label="Friends holding hands in warm evening light">
  <h2>Helping you find a flatshare<br>you can call home</h2>
</section>

<!-- New flatmates -->
<h2 class="section-title" style="top:2122px">New Flatmates</h2>
<div class="arrows" style="top:2125px">
  <span><svg width="8" height="10"><path d="M6 1L2 5l4 4" fill="none" stroke="#fff" stroke-width="2"/></svg></span>
  <span><svg width="8" height="10"><path d="M2 1l4 4-4 4" fill="none" stroke="#fff" stroke-width="2"/></svg></span>
</div>
<div class="cards" style="top:2178px">
  <article class="card">
    <div class="card-photo" role="img" aria-label="Two friends in winter hats" style="height:134px;background:linear-gradient(135deg,#b7c7d3,#8a5c8e 55%,#e2d6c8)"></div>
    <div class="card-bar" style="height:29px"><span class="who"><svg width="12" height="12" viewBox="0 0 12 12"><circle cx="6" cy="3.5" r="3" fill="#fff"/><path d="M0 12c0-4 3-5 6-5s6 1 6 5z" fill="#fff"/></svg>Lorem Ipsu 31</span></div>
    <p class="card-text">In publishing and graphic design, lorem ipsum is a filler text commonly used to demonstrate the graphic elements of a document or visual presentation.</p>
  </article>
  <article class="card">
    <div class="card-photo" role="img" aria-label="Flatmates relaxing on a sofa" style="height:134px;background:linear-gradient(135deg,#6a5140,#3a2e28 55%,#9b8370)"></div>
    <div class="card-bar" style="height:29px"><span class="who"><svg width="12" height="12" viewBox="0 0 12 12"><circle cx="6" cy="3.5" r="3" fill="#fff"/><path d="M0 12c0-4 3-5 6-5s6 1 6 5z" fill="#fff"/></svg>Lorem Ipsu 31</span></div>
    <p class="card-text">In publishing and graphic design, lorem ipsum is a filler text commonly used to demonstrate the graphic elements of a document or visual presentation.</p>
  </article>
  <article class="card">
    <div class="card-photo" role="img" aria-label="Group of young friends smiling" style="height:134px;background:linear-gradient(135deg,#e8e3dc,#c48b5e 50%,#7c8fa6)"></div>
    <div class="card-bar" style="height:29px"><span class="who"><svg width="12" height="12" viewBox="0 0 12 12"><circle cx="6" cy="3.5" r="3" fill="#fff"/><path d="M0 12c0-4 3-5 6-5s6 1 6 5z" fill="#fff"/></svg>Lorem Ipsu 31</span></div>
    <p class="card-text">In publishing and graphic design, lorem ipsum is a filler text commonly used to demonstrate the graphic elements of a document or visual presentation.</p>
  </article>
  <article class="card">
    <div class="card-photo" role="img" aria-label="Friends lying together on a bed" style="height:134px;background:linear-gradient(135deg,#d7e4ee,#f2e6dc 50%,#c58c6c)"></div>
    <div class="card-bar" style="height:29px"><span class="who"><svg width="12" height="12" viewBox="0 0 12 12"><circle cx="6" cy="3.5" r="3" fill="#fff"/><path d="M0 12c0-4 3-5 6-5s6 1 6 5z" fill="#fff"/></svg>Lorem Ipsu 31</span></div>
    <p class="card-text">In publishing and graphic design, lorem ipsum is a filler text commonly used to demonstrate the graphic elements of a document or visual presentation.</p>
  </article>
</div>

<!-- CTA -->
<section class="cta">
  <h2>Find your perfect flatshare today!</h2>
  <div class="cta-buttons">
    <div class="btn btn-orange">Start your search</div>
    <div class="btn btn-pink">Post your room</div>
  </div>
</section>

<!-- Footer -->
<footer class="footer">
  <div class="foot-col" style="left:72px">
    <h4>Popular Cities</h4>
    <ul>
      <li>Birmingham flatshare</li><li>Bristol flatshare</li><li>Coventry flatshare</li><li>Leeds flatshare</li><li>Liverpool flatshare</li><li>London flatshare</li><li>Manchester flatshare</li><li>Newcastle upon Tyne flatshare</li><li>Nottingham flatshare</li><li>Sheffield flatshare</li><li class="all">All cities</li>
    </ul>
  </div>
  <div class="foot-col" style="left:342px">
    <h4>Flatshare Types</h4>
    <ul>
      <li>Bedsits And Studios</li><li>Double Room Flatshare</li><li>DSS</li><li>Female Flatshare</li><li>Monday to Friday</li><li>Professional Flatshare</li><li>Roomshare</li><li>Short Let</li><li>Single Room Flatshare</li><li>Spare Room And Lodger</li><li>Student Accommodation</li>
    </ul>
  </div>
  <div class="foot-col" style="left:613px">
    <h4>About Us</h4>
    <ul>
      <li>Need help?</li><li>FAQs</li><li>Press Room</li><li>Website Visitor &amp; User Agreements</li><li>Right-To-Rent</li><li>Become an Affiliate</li><li>Our Pledge</li>
    </ul>
  </div>
  <div class="foot-col" style="left:883px">
    <h4>Discover</h4>
    <ul><li>Landlord Zone</li><li>Our Blog</li></ul>
    <h4 style="margin-top:22px">Stay Connected</h4>
    <div class="socials"><span></span><span></span><span></span><span></span><span></span></div>
  </div>
  <div class="foot-bottom">
    <span>©2015 - Cmpany Name here. All Rights Reserved.</span>
    <nav><span>Privacy Policy</span><span>Terms of Use</span></nav>
  </div>
</footer>

</body>
</html>
```